Rising Paths Web Design

I am starting a new company that will provide LIFE COACHING services - I have tried to design a website, but it's too complicated. Right now, it's just me - I'm the only person that will provide services through the website - I have used artmarket to purchase a logo (see below). I want to be able to update the website myself, but need a template - basic design. Because I am not technologically savvy enough to explain in words - I basically want to have a website that will provide basic information about my services (coaching), a page about me and my background, hopefully scheduling possibilities, and testimonials — also a page for writing/blogs. I bought a website through NetHarbor - so when I have a template, I guess I”d use that - but maybe I’ll need to work with a designer to actually get it up on the internet. I have a head shot that I’ll upload, too.
Target Market(s)
Clients from the independent (private school) world - teachers, administrators
Number of Pages Required
4 page
Look and feel
Each slider illustrates characteristics of the customer's brand and the style your logo design should communicate.

```html
<!DOCTYPE html>
<html lang="en">
<head>
<meta charset="utf-8">
<title>Rising Paths Coaching</title>
<link rel="stylesheet" href="https://fonts.googleapis.com/css2?family=Cinzel:wght@500;600;700&family=Montserrat:wght@500&family=Playfair+Display:wght@400;500&display=swap">
<style>
  :root {
    --teal: #1ba596;
    --teal-deep: #0e7c70;
    --teal-soft: #9fdcd3;
    --mint: #eef9f7;
    --ink: #111111;
    --white: #ffffff;
    --sky-top: #9cc3db;
    --sky-mid: #6f8799;
    --sky-low: #3e4a58;
  }
  * { box-sizing: border-box; margin: 0; padding: 0; }
  html, body { width: 1200px; height: 4155px; overflow: hidden; }
  body {
    position: relative;
    background: var(--mint);
    font-family: "Playfair Display", Georgia, serif;
    color: var(--ink);
  }
  .abs { position: absolute; }

  /* Hero */
  .hero-photo {
    left: 0; top: 0; width: 1200px; height: 830px;
    background: linear-gradient(180deg, var(--sky-top) 0%, #c9dbe6 28%, var(--sky-mid) 55%, var(--sky-low) 80%, #2b3038 100%);
  }
  .hero-wave { left: 0; top: 640px; width: 1200px; height: 200px; }
  .brand {
    font-family: "Cinzel", serif; font-weight: 600; font-size: 22px;
    color: var(--ink); display: flex; align-items: center; gap: 12px; white-space: nowrap;
  }
  .brand-dot { width: 14px; height: 14px; border-radius: 50%; background: var(--teal); }
  .header-brand { left: 121px; top: 76px; }
  .btn-schedule {
    left: 889px; top: 23px; width: 209px; height: 37px; border-radius: 19px;
    background: var(--teal); color: var(--white);
    font-family: "Cinzel", serif; font-size: 12px; font-weight: 600;
    display: flex; align-items: center; justify-content: center; letter-spacing: .3px;
  }
  .main-nav { top: 77px; left: 0; width: 1200px; height: 20px; }
  .main-nav a {
    position: absolute; font-family: "Cinzel", serif; font-size: 13px; font-weight: 600;
    color: var(--ink); text-decoration: none; white-space: nowrap;
  }
  .main-nav a.active { color: var(--teal); }
  .hero-title {
    left: 126px; top: 280px; font-family: "Cinzel", serif; font-weight: 700;
    font-size: 46px; letter-spacing: 1px; line-height: 1; white-space: nowrap;
  }
  .hero-sub {
    left: 129px; top: 337px; font-family: "Montserrat", sans-serif; font-weight: 500;
    font-size: 31px; letter-spacing: 7px; color: var(--teal);
  }
  .btn {
    position: absolute; border-radius: 22px; display: flex; align-items: center; justify-content: center;
    font-family: "Cinzel", serif; font-weight: 600; font-size: 18px; letter-spacing: .4px; white-space: nowrap;
  }
  .btn-fill { background: var(--teal); color: var(--white); }
  .btn-line { background: var(--white); color: var(--ink); border: 2px solid var(--teal); }

  /* Circular photo slots */
  .photo-ring { border-radius: 50%; border: 3px solid var(--teal); }
  .photo-disc { border-radius: 50%; }
  .ornament { border-radius: 50%; background: radial-gradient(circle, rgba(27,165,150,.35), rgba(27,165,150,0)); }

  .section-title {
    position: absolute; font-family: "Cinzel", serif; font-weight: 700; font-size: 41px;
    line-height: 1.1; border-bottom: 2px solid currentColor; padding-bottom: 2px; white-space: nowrap;
  }
  .body-copy { position: absolute; font-size: 11.6px; line-height: 22.6px; white-space: nowrap; }

  /* Testimonials */
  .testimonial-band { left: 0; top: 1740px; width: 1200px; height: 930px; }
  .avatar {
    position: absolute; width: 120px; height: 120px; border-radius: 50%;
    border: 3px solid var(--white); background: linear-gradient(180deg, #f2f2f2, #cfd6d8);
  }
  .quote {
    position: absolute; color: var(--white); font-size: 16px; line-height: 26px; white-space: nowrap;
  }
  .quote-name {
    position: absolute; color: var(--white); font-family: "Cinzel", serif; font-weight: 600; font-size: 20px; white-space: nowrap;
  }
  .slider-arrow { position: absolute; width: 42px; height: 42px; }

  /* Blog */
  .post { position: absolute; width: 340px; text-align: center; }
  .post-photo { width: 306px; height: 306px; margin: 0 auto; border-radius: 50%; box-shadow: 0 6px 14px rgba(0,0,0,.18); }
  .post-title { margin-top: 30px; font-family: "Cinzel", serif; font-weight: 600; font-size: 20px; }
  .post-text { margin-top: 6px; font-size: 14px; line-height: 22px; color: #333; white-space: nowrap; }
  .post-date {
    margin-top: 12px; display: flex; justify-content: center; align-items: center; gap: 10px;
    font-family: "Cinzel", serif; font-weight: 600; font-size: 20px;
  }

  /* Footer */
  .footer-band { left: 0; top: 3560px; width: 1200px; height: 595px; }
  .footer-brand { left: 140px; top: 3905px; color: var(--white); }
  .footer-brand .brand-dot { background: var(--white); }
  .footer-ring { left: 132px; top: 3830px; width: 190px; height: 190px; border-radius: 50%; border: 2px solid rgba(255,255,255,.7); }
  .footer-col h3 {
    font-family: "Cinzel", serif; font-weight: 600; font-size: 20px; color: var(--white); margin-bottom: 14px; white-space: nowrap;
  }
  .footer-col ul { list-style: none; }
  .footer-col li {
    color: var(--white); font-size: 14px; line-height: 25.8px; padding-left: 20px; position: relative; white-space: nowrap;
  }
  .footer-col li::before {
    content: ""; position: absolute; left: 2px; top: 11px; width: 7px; height: 7px; border-radius: 50%; background: var(--white);
  }
  .field {
    position: absolute; left: 873px; width: 225px; height: 42px; border-radius: 21px; background: var(--white);
    font-family: "Montserrat", sans-serif; font-size: 10px; color: #555; padding-left: 20px;
    display: flex; align-items: center; letter-spacing: .5px;
  }
  .btn-submit {
    left: 877px; top: 3984px; width: 102px; height: 32px; border-radius: 16px; background: #000; color: var(--white);
    font-family: "Cinzel", serif; font-weight: 700; font-size: 14px; display: flex; align-items: center; justify-content: center;
  }
  .copyright { left: 0; top: 4097px; width: 1200px; text-align: center; color: var(--white); font-size: 13px; }
</style>
</head>
<body>

<!-- Hero -->
<div class="abs hero-photo" role="img" aria-label="Hiker with a backpack raising both arms on a rocky summit under a cloudy sky"></div>
<svg class="abs hero-wave" viewBox="0 0 1200 200" preserveAspectRatio="none" aria-hidden="true">
  <path d="M0 70 C250 160 480 200 700 170 C900 140 1080 100 1200 50 L1200 200 L0 200 Z" fill="var(--teal)"/>
  <path d="M0 82 C250 170 480 188 700 160 C900 134 1080 105 1200 75 L1200 200 L0 200 Z" fill="var(--white)"/>
  <path d="M0 92 C250 178 480 176 700 148 C900 124 1080 110 1200 98 L1200 200 L0 200 Z" fill="var(--mint)"/>
</svg>
<div class="abs ornament" style="left:30px;top:580px;width:360px;height:250px;" role="img" aria-label="Teal leaf branch ornament"></div>

<div class="abs brand header-brand"><span class="brand-dot"></span>Rising Paths</div>
<div class="abs btn-schedule">SCHEDULE APPOINTMENT</div>
<nav class="abs main-nav">
  <a class="active" href="#" style="left:489px">HOME</a>
  <a href="#" style="left:561px">SERVICES</a>
  <a href="#" style="left:658px">ABOUT ME</a>
  <a href="#" style="left:763px">MY BACKGROUND</a>
  <a href="#" style="left:924px">TESTIMONIALS</a>
  <a href="#" style="left:1060px">BLOG</a>
</nav>
<h1 class="abs hero-title">RISING PATHS</h1>
<div class="abs hero-sub">COACHING</div>
<div class="btn btn-fill" style="left:129px;top:392px;width:211px;height:43px;">GET IN TOUCH</div>

<!-- About -->
<div class="abs ornament" style="left:300px;top:870px;width:300px;height:200px;" role="img" aria-label="Teal leaf branch ornament"></div>
<div class="abs photo-ring" style="left:100px;top:912px;width:472px;height:472px;"></div>
<div class="abs photo-disc" style="left:112px;top:920px;width:452px;height:452px;background:linear-gradient(160deg,#7d8f97,#3f4a52 60%,#8aa0ab);" role="img" aria-label="Head shot of the coach smiling at her desk"></div>
<h2 class="section-title" style="left:682px;top:1044px;">ABOUT ME</h2>
<p class="body-copy" style="left:680px;top:1127px;">Lorem ipsum dolor sit amet, consectetur adipiscing elit, sed do<br>eiusmod tempor incididunt ut labore et dolore magna aliqua. Ut enim<br>ad minim veniam, quis nostrud exercitation ullamco laboris nisi ut<br>aliquip ex ea commodo consequat. Duis aute irure dolor in<br>reprehenderit in voluptate velit esse cillum dolore eu fugiat nulla<br>pariatur. Excepteur sint occaecat cupidatat non proident, sunt in culpa<br>qui officia deserunt mollit anim id est laborum.</p>
<div class="btn btn-fill" style="left:679px;top:1308px;width:163px;height:42px;">READ MORE</div>
<div class="btn btn-line" style="left:861px;top:1308px;width:192px;height:42px;">BOOK SESSION</div>

<!-- Teal testimonial band -->
<svg class="abs testimonial-band" viewBox="0 0 1200 930" preserveAspectRatio="none" aria-hidden="true">
  <defs>
    <linearGradient id="bandFill" x1="0" y1="0" x2="1" y2="1">
      <stop offset="0" stop-color="#17a091"/>
      <stop offset=".6" stop-color="#22ada0"/>
      <stop offset="1" stop-color="#1aa596"/>
    </linearGradient>
  </defs>
  <path d="M0 305 C400 320 800 200 1200 18 L1200 930 L0 930 Z" fill="url(#bandFill)"/>
  <path d="M0 900 C300 830 600 780 900 800 C1020 808 1120 830 1200 850 L1200 930 L0 930 Z" fill="var(--white)"/>
  <path d="M0 914 C300 846 600 800 900 818 C1020 826 1120 846 1200 864 L1200 930 L0 930 Z" fill="var(--mint)"/>
</svg>

<!-- Our coaching -->
<h2 class="section-title" style="left:106px;top:1605px;">OUR COACHING</h2>
<p class="body-copy" style="left:106px;top:1692px;">Lorem ipsum dolor sit amet, consectetur adipiscing elit, sed do<br>eiusmod tempor incididunt ut labore et dolore magna aliqua. Ut enim<br>ad minim veniam, quis nostrud exercitation ullamco laboris nisi ut<br>aliquip ex ea commodo consequat. Duis aute irure dolor in<br>reprehenderit in voluptate velit esse cillum dolore eu fugiat nulla<br>pariatur. Excepteur sint occaecat cupidatat non proident, sunt in culpa<br>qui officia deserunt mollit anim id est laborum.</p>
<div class="btn btn-fill" style="left:103px;top:1869px;width:165px;height:44px;">READ MORE</div>
<div class="btn btn-line" style="left:287px;top:1869px;width:192px;height:44px;">BOOK SESSION</div>
<div class="abs ornament" style="left:800px;top:1420px;width:340px;height:260px;" role="img" aria-label="Teal leaf branch ornament"></div>
<div class="abs photo-ring" style="left:632px;top:1530px;width:472px;height:472px;"></div>
<div class="abs photo-disc" style="left:644px;top:1540px;width:452px;height:452px;background:linear-gradient(170deg,#e6ecef,#b9c4c8 45%,#5b6266 80%,#cfd6d8);" role="img" aria-label="Two women talking across a table during a coaching session"></div>

<!-- Testimonials -->
<h2 class="section-title" style="left:421px;top:2165px;color:var(--white);">TESTIMONIALS</h2>
<svg class="slider-arrow" style="left:27px;top:2337px;" viewBox="0 0 42 42" aria-hidden="true">
  <circle cx="21" cy="21" r="19" fill="none" stroke="rgba(255,255,255,.75)" stroke-width="2"/>
  <path d="M24 13 L16 21 L24 29" fill="none" stroke="rgba(255,255,255,.85)" stroke-width="2"/>
</svg>
<svg class="slider-arrow" style="left:1134px;top:2337px;" viewBox="0 0 42 42" aria-hidden="true">
  <circle cx="21" cy="21" r="19" fill="none" stroke="rgba(255,255,255,.75)" stroke-width="2"/>
  <path d="M18 13 L26 21 L18 29" fill="none" stroke="rgba(255,255,255,.85)" stroke-width="2"/>
</svg>
<div class="avatar" style="left:106px;top:2298px;" role="img" aria-label="Portrait of client Tomas Rivello"></div>
<p class="quote" style="left:271px;top:2294px;">"Lorem ipsum dolor sit amet, consectetur<br>adipiscing elit, sed do eiusmod tempor<br>incididunt ut labore et dolore magna<br>aliquaenim adlaborum."</p>
<div class="quote-name" style="left:271px;top:2415px;">- TOMAS RIVELLO</div>
<div class="avatar" style="left:635px;top:2298px;" role="img" aria-label="Portrait of client Marielle Dawn"></div>
<p class="quote" style="left:798px;top:2294px;">"Lorem ipsum dolor sit amet, consectetur<br>adipiscing elit, sed do eiusmod tempor<br>incididunt ut labore et dolore magna<br>aliquaenim adlaborum."</p>
<div class="quote-name" style="left:798px;top:2415px;">- MARIELLE DAWN</div>
<div class="abs ornament" style="left:60px;top:2500px;width:420px;height:300px;" role="img" aria-label="Teal leaf branch ornament"></div>

<!-- Latest blog -->
<h2 class="section-title" style="left:456px;top:2806px;">LATEST BLOG</h2>
<article class="post" style="left:83px;top:2952px;">
  <div class="post-photo" style="background:linear-gradient(160deg,#d9c3a8,#a88a6c 50%,#efe6dc);" role="img" aria-label="Coach meeting a client at a bright table"></div>
  <h3 class="post-title">LOREM IPSUM DOLOR</h3>
  <p class="post-text">Lorem ipsum dolor sit amet, consectet<br>ur adipiscing elit, sed do eiusmod tempor<br>incididunt ut labore et doloaliqua.</p>
  <div class="post-date"><svg width="28" height="28" viewBox="0 0 28 28" aria-hidden="true"><rect x="3" y="5" width="22" height="20" rx="2" fill="none" stroke="var(--teal)" stroke-width="2"/><path d="M3 11 H25 M9 2 V8 M19 2 V8" stroke="var(--teal)" stroke-width="2"/><path d="M8 15h3M13 15h3M18 15h3M8 20h3M13 20h3" stroke="var(--teal)" stroke-width="2"/></svg>12.06.2022</div>
</article>
<article class="post" style="left:427px;top:2952px;">
  <div class="post-photo" style="background:linear-gradient(170deg,#cfcfcf,#7a746e 50%,#e4ddd2);" role="img" aria-label="Two women reading notes together in an office"></div>
  <h3 class="post-title">LOREM IPSUM DOLOR</h3>
  <p class="post-text">Lorem ipsum dolor sit amet, consectet<br>ur adipiscing elit, sed do eiusmod tempor<br>incididunt ut labore et doloaliqua.</p>
  <div class="post-date"><svg width="28" height="28" viewBox="0 0 28 28" aria-hidden="true"><rect x="3" y="5" width="22" height="20" rx="2" fill="none" stroke="var(--teal)" stroke-width="2"/><path d="M3 11 H25 M9 2 V8 M19 2 V8" stroke="var(--teal)" stroke-width="2"/><path d="M8 15h3M13 15h3M18 15h3M8 20h3M13 20h3" stroke="var(--teal)" stroke-width="2"/></svg>03.07.2022</div>
</article>
<article class="post" style="left:777px;top:2952px;">
  <div class="post-photo" style="background:linear-gradient(180deg,#cbd8df,#e8eef0 45%,#95a6ad 75%,#6f6a62);" role="img" aria-label="Woman sitting on a rock above a misty valley"></div>
  <h3 class="post-title">LOREM IPSUM DOLOR</h3>
  <p class="post-text">Lorem ipsum dolor sit amet, consectet<br>ur adipiscing elit, sed do eiusmod tempor<br>incididunt ut labore et doloaliqua.</p>
  <div class="post-date"><svg width="28" height="28" viewBox="0 0 28 28" aria-hidden="true"><rect x="3" y="5" width="22" height="20" rx="2" fill="none" stroke="var(--teal)" stroke-width="2"/><path d="M3 11 H25 M9 2 V8 M19 2 V8" stroke="var(--teal)" stroke-width="2"/><path d="M8 15h3M13 15h3M18 15h3M8 20h3M13 20h3" stroke="var(--teal)" stroke-width="2"/></svg>22.07.2022</div>
</article>

<!-- Footer -->
<svg class="abs footer-band" viewBox="0 0 1200 595" preserveAspectRatio="none" aria-hidden="true">
  <path d="M0 140 C300 120 550 180 800 140 C950 116 1080 90 1200 60 L1200 595 L0 595 Z" fill="var(--teal-deep)"/>
</svg>
<div class="abs ornament" style="left:20px;top:3550px;width:520px;height:300px;" role="img" aria-label="Teal leaf branch ornament"></div>
<div class="abs footer-ring"></div>
<div class="abs brand footer-brand"><span class="brand-dot"></span>Rising Paths</div>

<div class="abs footer-col" style="left:432px;top:3830px;">
  <h3>NAVIGATION</h3>
  <ul><li>Home</li><li>Coaching</li><li>About me</li><li>My background</li><li>Scheduling</li><li>Testimonials</li><li>Blogs</li></ul>
</div>
<div class="abs footer-col" style="left:656px;top:3830px;">
  <h3>SERVICES</h3>
  <ul><li>Lorem ipsum</li><li>Dolor sit amet,</li><li>Consectetur</li><li>Adipiscing elit,</li><li>Sed dousmod</li><li>Tmpor</li><li>Dolor sit amet,</li></ul>
</div>
<div class="abs footer-col" style="left:876px;top:3830px;"><h3>GET IN TOUCH</h3></div>
<div class="field" style="top:3871px;">NAME</div>
<div class="field" style="top:3928px;">EMAIL ADDRESS</div>
<div class="abs btn-submit">SUBMIT</div>
<p class="abs copyright">© 2022 All Rights Reserved.Terms &amp; Conditions Privacy Policy</p>

</body>
</html>
```